I need a simple, classy and stylish business card. I would like it to have a black background with white writing. I would like you to use my logo you designed on the front with the word 'Imagery" used underneath it in the same font. On the back I was thinking of the website at the top 'tomverrick.com' Then my social media accounts, Can you use the instagram, Facebook and twitter logo then my handles?
Please let me know what you think.
Regards Tom
Must have
- Website: www.tomverrick.com
- Social media handles..
- Instagram: @Tom_Verrick_Imagery
- Facebook: Tom Verrick Imagery
- Twitter: @Tom_Verrick
- Email: info@tomverick.com
- Phone: 0437 518 293

```html
<!DOCTYPE html>
<html lang="en">
<head>
<meta charset="utf-8">
<title>Tom Verrick Imagery – Business Card</title>
<link rel="stylesheet" href="https://fonts.googleapis.com/css2?family=Nothing+You+Could+Do&family=Open+Sans:wght@400;600&display=swap">
<style>
  :root {
    --stage-top: #c9c9c9;
    --stage-bottom: #ffffff;
    --card: #000000;
    --ink: #ffffff;
    --ink-soft: #e6e6e6;
  }
  * { margin: 0; padding: 0; box-sizing: border-box; }
  html, body { width: 1200px; height: 900px; overflow: hidden; }
  body {
    position: relative;
    background: linear-gradient(180deg, var(--stage-top) 0%, #e4e4e4 55%, var(--stage-bottom) 100%);
    font-family: "Open Sans", Arial, sans-serif;
  }
  .card {
    position: absolute;
    top: 306px;
    width: 440px;
    height: 271px;
    background: var(--card);
    border-radius: 12px;
    color: var(--ink);
    overflow: hidden;
  }
  .card--front { left: 149px; }
  .card--back { left: 608px; }

  .brand {
    font-family: "Nothing You Could Do", cursive;
    color: var(--ink);
    font-weight: 400;
    line-height: 1;
  }
  .front-brand {
    position: absolute;
    left: 160px;
    top: 146px;
    display: flex;
    align-items: center;
    gap: 14px;
  }
  .front-brand .mark {
    width: 44px;
    height: 44px;
    border-radius: 50%;
    border: 3px solid var(--ink);
    flex: none;
  }
  .front-brand .brand { font-size: 30px; }
  .front-brand .brand span { display: block; font-size: 20px; margin: 4px 0 0 44px; }

  .back-brand {
    position: absolute;
    top: 44px;
    left: 0;
    width: 100%;
    text-align: center;
    font-size: 34px;
  }
  .back-brand span { display: block; font-size: 20px; margin: 2px 0 0 -10px; }

  .handles {
    position: absolute;
    top: 140px;
    left: 0;
    width: 100%;
    list-style: none;
    text-align: center;
    font-size: 12.5px;
    line-height: 21.5px;
  }
  .handles li { display: flex; justify-content: center; align-items: center; gap: 6px; }
  .handles .icon {
    width: 12px;
    height: 12px;
    background: var(--ink);
    border-radius: 2px;
    flex: none;
  }
  .website {
    position: absolute;
    top: 220px;
    left: 0;
    width: 100%;
    text-align: center;
    font-size: 13.5px;
    font-weight: 600;
    color: var(--ink-soft);
  }
</style>
</head>
<body>
  <section class="card card--front" aria-label="Card front">
    <div class="front-brand">
      <span class="mark" aria-hidden="true"></span>
      <p class="brand">Tom Verrick<span>Imagery</span></p>
    </div>
  </section>

  <section class="card card--back" aria-label="Card back">
    <p class="brand back-brand">Tom Verrick<span>Imagery</span></p>
    <ul class="handles">
      <li><span class="icon" aria-hidden="true"></span>@Tom_Verrick_Imagery</li>
      <li><span class="icon" aria-hidden="true"></span>@TomVerrickImagery</li>
      <li><span class="icon" aria-hidden="true"></span>@Tom_Verrick</li>
    </ul>
    <p class="website">www.tomverrick.com</p>
  </section>
</body>
</html>
```